Derek Amblewood needs a single album cover

I need an single album cover for a song I wrote called "Quiet Harbor". I would like the design to Illustrate how gods grace covers all sin.

Requirements
Must have
• The song title "Quiet Harbor" And my name Derek Amblewood

```html
<!DOCTYPE html>
<html lang="en">
<head>
<meta charset="utf-8">
<title>Quiet Harbor — Derek Amblewood</title>
<link href="https://fonts.googleapis.com/css2?family=Cinzel:wght@400;600&display=swap" rel="stylesheet">
<style>
  :root {
    --backdrop: #000000;
    --sky-deep: #101c33;
    --sky-mid: #3d5578;
    --sky-light: #a9b8cc;
    --glow: #e8eef4;
    --frame-line: rgba(215, 222, 232, 0.7);
    --type-white: #ffffff;
    --type-shadow: rgba(10, 20, 40, 0.55);
  }
  * { margin: 0; padding: 0; box-sizing: border-box; }
  html, body {
    width: 1200px;
    height: 1000px;
    overflow: hidden;
    background: var(--backdrop);
  }
  .canvas {
    position: relative;
    width: 1200px;
    height: 1000px;
    background: var(--backdrop);
  }
  .cover {
    position: absolute;
    left: 170px;
    top: 68px;
    width: 862px;
    height: 862px;
    overflow: hidden;
  }
  .cover-sky {
    position: absolute;
    inset: 0;
    background:
      radial-gradient(ellipse 30% 26% at 60% 42%, var(--glow) 0%, rgba(232,238,244,0) 100%),
      radial-gradient(ellipse 60% 55% at 52% 45%, var(--sky-light) 0%, rgba(169,184,204,0) 80%),
      radial-gradient(ellipse 80% 80% at 50% 50%, var(--sky-mid) 0%, var(--sky-deep) 100%);
  }
  .cover-frame {
    position: absolute;
    inset: 0;
  }
  .artist-name {
    position: absolute;
    top: 22px;
    left: 0;
    width: 100%;
    text-align: center;
    font-family: "Cinzel", serif;
    font-weight: 400;
    font-size: 21px;
    letter-spacing: 0.36em;
    color: var(--glow);
    text-transform: uppercase;
  }
  .song-title {
    position: absolute;
    left: 0;
    width: 100%;
    text-align: center;
    font-family: "Cinzel", serif;
    color: var(--type-white);
    text-transform: uppercase;
    line-height: 1;
    text-shadow: 2px 3px 4px var(--type-shadow), 0 0 1px rgba(0,0,0,0.4);
  }
  .song-title-first {
    top: 250px;
    font-size: 196px;
    font-weight: 600;
    letter-spacing: -0.02em;
  }
  .song-title-second {
    top: 585px;
    font-size: 132px;
    font-weight: 400;
    letter-spacing: 0.01em;
  }
</style>
</head>
<body>
  <main class="canvas">
    <section class="cover">
      <div class="cover-sky" role="img" aria-label="Dramatic blue cloudy sky with sunlight breaking through and the silhouette of a person raising one hand toward the light"></div>
      <svg class="cover-frame" width="862" height="862" viewBox="0 0 862 862" aria-hidden="true">
        <path d="M195 33 H27 V829 H830 V33 H667" fill="none" stroke="var(--frame-line)" stroke-width="2.5"/>
      </svg>
      <p class="artist-name">Derek Amblewood</p>
      <h1 class="song-title song-title-first">Quiet</h1>
      <h2 class="song-title song-title-second">Harbor</h2>
    </section>
  </main>
</body>
</html>
```